Coffee Roastery Label Sticker Design

We are starting a small Micro-Coffee-Roastery and are looking for a catchy design, which might look a bit hipster style, but not too much. It's called "lantern roastery", because we started roasting first in our backyard / garden by our house.
At the end of the logo and the details of the sticker (like all text elements) we need to be able to modify later by ourselfs. Coffee type, origin of coffee and so one ...
The label will be sticked on a white craftpaper coffee bag of 250grams. Sticker size around 8x12.5 cm.
The coffee bag should be an eye-catcher in a shop-shelve compared to the other coffee brands.
Another example that i really like (just to get you another idea of what we would love to get because we really like that style): https://pixvaultcdn.net/art_img/5172839/80412/61937204/qhrmzvle7k4b9x2d6wf1ny3u8p_image.png).
OR https://packfolioweb.net/blog/2016/3/14/ember-beans?

Target Market(s)

"0Speciality Coffee" lovers
High quality specialty coffee and a clear origin of the bean and fair trade or project coffee is what makes our roasted coffee product special

Logo Text

Laterne Rösterei

Requirements
Must have
• A house and a garden with either flowers or a tree is what we have in mind.
The printed label will be square 8x12.5 cm. We will use the logo on the printed label (we will print on our own printer) and on a homepage.
Nice to have
• In the attached logo example, there is no connection to a coffee business. Actually it would be a nice detail to include somehow either a descent coffee bean, a cup or a tiny roastery machine or whatever is in your mind with coffee ... (not a grinder)
Black and white is OK, but we also like colourfull very much
Please see the attached documents with sample designs that we created on our own with canvas. It's not too bad, but also a bit boring. If you have a completely different idea, please go for it. we are very open for other cool and hip designs or also quite descent and femail touch is fine too, but no must.

```html
<!DOCTYPE html>
<html lang="de">
<head>
<meta charset="utf-8">
<title>Laterne Rösterei – Etiketten</title>
<link rel="stylesheet" href="https://fonts.googleapis.com/css2?family=Bebas+Neue&display=swap">
<style>
  :root {
    --ink: #25323d;
    --paper: #ffffff;
    --gold: #bf9d63;
    --rust: #d45a36;
    --brown: #6a3214;
  }
  * { box-sizing: border-box; margin: 0; padding: 0; }
  html, body {
    width: 1028px;
    height: 1200px;
    overflow: hidden;
    background: var(--paper);
  }
  body {
    font-family: "Bebas Neue", "Oswald", sans-serif;
    color: var(--ink);
    display: flex;
    align-items: center;
    justify-content: center;
    gap: 38px;
  }
  .label {
    --accent: var(--rust);
    width: 300px;
    height: 470px;
    border: 1.5px solid var(--ink);
    position: relative;
    display: flex;
    flex-direction: column;
    align-items: center;
    padding: 34px 18px 18px;
  }
  .label--gold { --accent: var(--gold); }
  .label--rust { --accent: var(--rust); }
  .label--brown { --accent: var(--brown); }

  .brand {
    display: flex;
    flex-direction: column;
    align-items: center;
    height: 252px;
  }
  .brand__mark {
    width: 138px;
    height: 138px;
    border-radius: 50%;
    border: 2px solid var(--ink);
  }
  .brand__name {
    margin-top: 18px;
    font-size: 31px;
    letter-spacing: 2px;
    line-height: 1;
    color: var(--ink);
  }
  .brand__tagline {
    margin-top: 8px;
    font-size: 22px;
    letter-spacing: 2px;
    line-height: 1;
    color: var(--accent);
  }

  .product-band {
    width: 100%;
    background: var(--accent);
    color: var(--paper);
    text-align: center;
    padding: 6px 0 4px;
    font-size: 22px;
    line-height: 1.02;
    letter-spacing: 0.5px;
  }
  .roast {
    margin-top: 7px;
    font-size: 11.5px;
    letter-spacing: 0.4px;
    color: var(--accent);
  }
  .label--brown .roast { color: var(--ink); }

  .facts {
    align-self: flex-end;
    text-align: right;
    font-size: 11.5px;
    line-height: 1.2;
    letter-spacing: 0.3px;
    margin-right: 14px;
  }
  .origin {
    align-self: flex-start;
    margin-left: 68px;
    margin-top: 8px;
    font-size: 11.5px;
    line-height: 1.15;
    letter-spacing: 0.3px;
    color: var(--accent);
  }
</style>
</head>
<body>

  <article class="label label--gold">
    <header class="brand">
      <div class="brand__mark"></div>
      <p class="brand__name">Laterne Rösterei</p>
      <p class="brand__tagline">Specialty Coffee</p>
    </header>
    <h2 class="product-band">Filterkaffee<br>Äthiopien – Guji</h2>
    <p class="roast">Medium Roast</p>
    <ul class="facts" style="list-style:none">
      <li>250 Gramm</li>
      <li>Helle Röstung</li>
      <li>Kaffee aus Äthiopien</li>
      <li>100% Arabica | Whashed</li>
    </ul>
    <p class="origin">Geröstet in 8840 Tannwil<br>www.laterne-roesterei.ch</p>
  </article>

  <article class="label label--rust">
    <header class="brand">
      <div class="brand__mark"></div>
      <p class="brand__name">Laterne Rösterei</p>
      <p class="brand__tagline">Specialty Coffee</p>
    </header>
    <h2 class="product-band">Filterkaffee<br>Äthiopien – Guji</h2>
    <p class="roast">Medium Roast</p>
    <ul class="facts" style="list-style:none">
      <li>250 Gramm</li>
      <li>Helle Röstung</li>
      <li>Kaffee aus Äthiopien</li>
      <li>100% Arabica | Whashed</li>
    </ul>
    <p class="origin">Geröstet in 8840 Tannwil<br>www.laterne-roesterei.ch</p>
  </article>

  <article class="label label--brown">
    <header class="brand">
      <div class="brand__mark"></div>
      <p class="brand__name">Laterne Rösterei</p>
      <p class="brand__tagline">Specialty Coffee</p>
    </header>
    <h2 class="product-band">Filterkaffee<br>Äthiopien – Guji</h2>
    <p class="roast">Dark Roast</p>
    <ul class="facts" style="list-style:none">
      <li>250 Gramm</li>
      <li>Helle Röstung</li>
      <li>Kaffee aus Äthiopien</li>
      <li>100% Arabica | Whashed</li>
    </ul>
    <p class="origin">Geröstet in 8840 Tannwil<br>www.laterne-roesterei.ch</p>
  </article>

</body>
</html>
```